Flyer to advertise gutter cleaning throughout the Autumn and winter monthss

I need a new flyer to advertise gutter and driveway cleaning, roof and gutter repairs.

I am an experienced licensed Plumber and Gasfitter looking to broaden my scope of work to gutter cleaning. I am experienced in cleaning gutter and live in a area with large gum trees. I wont something that's clear, eye catching but not too busy.

Flyer requirements: Free roof inspection - no obligation. Gutter Cleaning from $199. Pictures of men using blower or hands to clean roof gutters (no obvious faces) to be included. Australian looking houses.

A mention that 'All general plumbing maintenance' is offered as other services but not too much wording about this as the target is for gutter cleaning.

Phone number: 0427 386 915 (in this format)
Business Name: Bellvane Plumbing & Gasfitting
License: 3174520
ABN: 71904352816
Web: http://bellvaneplumbing.example-site.net/

Target Market(s)

Elderly - busy working class

Industry/Entity Type

Plumber

Font styles to use
Sans Serif

Colors
0355a3
fbed22
ec1f27
f78f20

Requirements
Must have
• Roof Gutter Cleaning pictures
• Men in protective clothing if possible
Nice to have
• More information:
• Prevent against flooding, mold, rust, rotting and corrosion now!
• Gutter Cleaning Services
• • Remove leaves, sticks, and other debris
• • Clear away clogs
• • Test your downpipes
• • Pinpoint any gutter issues
• • Repair gutter
• With regular service, you can count on your property to be well-protected no matter what the forecast!
Should not have
• Houses that don't look Australian

```html
<!DOCTYPE html>
<html lang="en">
<head>
<meta charset="utf-8">
<title>Bellvane Plumbing & Gasfitting – Gutter Cleaning Flyer</title>
<link href="https://fonts.googleapis.com/css2?family=Oswald:wght@500;700&family=Lato:wght@400;700;900&display=swap" rel="stylesheet">
<style>
:root{
  --blue:#0355a3;
  --blue-deep:#0a4fa8;
  --blue-light:#1d6fd0;
  --red:#ec1f27;
  --yellow:#fbed22;
  --grey-text:#58595b;
  --dark:#231f20;
  --stage:#e9ecef;
  --white:#ffffff;
}
*{margin:0;padding:0;box-sizing:border-box}
html,body{width:1200px;height:1200px;overflow:hidden;background:var(--stage)}
.flyer{position:absolute;left:179px;top:6px;width:842px;height:1188px;background:var(--white);overflow:hidden;font-family:'Lato',sans-serif}
.shapes{position:absolute;left:0;top:0}
.badge{position:absolute;left:600px;top:286px;width:210px;height:210px;border-radius:50%;background:var(--white);border:5px solid var(--yellow);box-shadow:0 0 0 3px var(--white),0 2px 6px rgba(0,0,0,.15);text-align:center;font-family:'Oswald',sans-serif;padding-top:46px;z-index:3}
.badge-free{color:var(--red);font-size:66px;font-weight:700;line-height:.95;letter-spacing:1px}
.badge-line{font-size:20px;font-weight:700;line-height:1.2}
.badge-line.blue{color:var(--blue)}
.badge-line.dark{color:var(--dark)}
.brand{position:absolute;left:36px;top:500px;display:flex;align-items:center;gap:14px}
.brand-dot{width:62px;height:62px;border-radius:50%;background:var(--blue);flex:none}
.brand-name{font-size:22px;font-weight:700;color:var(--dark);line-height:1.15}
.headline{position:absolute;left:38px;top:612px;width:330px;height:276px;font-family:'Oswald',sans-serif;font-weight:700;text-transform:uppercase}
.headline span{position:absolute;left:0;white-space:nowrap;transform:scaleX(.88);transform-origin:left top;line-height:1}
.headline .grey{color:var(--grey-text);font-size:44px}
.headline .blue{color:var(--blue);font-size:80px}
.headline .line-1{top:0}
.headline .line-2{top:48px}
.headline .line-3{top:136px}
.headline .line-4{top:186px}
.other-services{position:absolute;left:38px;top:908px;width:332px;font-size:16px;color:var(--grey-text);line-height:1.28}
.call{position:absolute;left:92px;top:992px;width:206px;height:74px;border:2px solid #cfd2d4;border-radius:10px;text-align:center;box-shadow:0 4px 5px rgba(0,0,0,.12)}
.call-label{font-size:27px;color:var(--grey-text);margin-top:4px}
.call-number{font-size:24px;color:var(--red);display:flex;align-items:center;justify-content:center;gap:8px;font-weight:700}
.call-icon{width:20px;height:20px}
.info-panel{position:absolute;left:432px;top:470px;width:372px;height:418px;background:linear-gradient(180deg,var(--blue-light),var(--blue-deep));border-radius:0 0 12px 12px;color:var(--white);padding:52px 22px 0 28px;z-index:2}
.info-lead{font-size:19px;font-weight:700;line-height:1.28}
.info-sub{color:var(--yellow);font-size:17px;font-weight:700;margin:22px 0 8px}
.checklist{list-style:none;font-size:16.5px}
.checklist li{display:flex;align-items:center;gap:11px;height:31px;padding-left:4px}
.checklist svg{width:14px;height:14px;flex:none}
.info-close{font-size:19px;line-height:1.28;text-align:justify;margin-top:18px}
.price{position:absolute;left:445px;top:915px;width:346px;height:137px;background:#c9cacc;box-shadow:0 6px 6px rgba(0,0,0,.12)}
.price-inner{position:absolute;inset:12px 16px;border:2px dashed #eeeeee;text-align:center}
.price-label{font-size:25px;font-weight:700;color:var(--grey-text);margin-top:14px;letter-spacing:.5px}
.price-amount{font-family:'Oswald',sans-serif;font-weight:700;font-size:50px;color:var(--grey-text);line-height:1.05}
.price-amount span{color:var(--red)}
.footer{position:absolute;left:0;bottom:0;width:842px;height:80px;color:var(--white);text-align:center;z-index:2}
.footer-name{font-size:17px;font-weight:700;margin-top:6px}
.footer-details{display:flex;justify-content:center;gap:48px;font-size:16px;margin-top:14px}
.footer-details b{font-weight:900}
</style>
</head>
<body>
<main class="flyer">
  <svg class="shapes" width="842" height="1188" viewBox="0 0 842 1188">
    <defs>
      <linearGradient id="photoTone" x1="0" y1="1" x2="1" y2="0">
        <stop offset="0" stop-color="#4e545c"/>
        <stop offset=".45" stop-color="#c9a64a"/>
        <stop offset=".75" stop-color="#7a9a3a"/>
        <stop offset="1" stop-color="#1f2a44"/>
      </linearGradient>
    </defs>
    <path role="img" aria-label="Gloved hands clearing autumn leaves from a roof gutter" fill="url(#photoTone)" d="M0 0H842V290C700 382 560 436 420 436C250 436 110 410 0 382Z"/>
    <path fill="var(--blue)" d="M0 382C110 410 250 436 420 436C560 436 700 382 842 290V316C700 420 560 462 420 462C250 462 110 440 0 412Z"/>
    <path fill="var(--red)" d="M420 462C560 462 700 420 842 316V336C700 436 560 472 420 468Z"/>
    <path fill="var(--blue)" d="M0 1118C200 1082 480 1068 720 1090L720 1096C480 1076 200 1090 0 1126Z"/>
    <path fill="var(--red)" d="M200 1084C420 1062 640 1070 842 1112V1124C640 1080 420 1070 200 1090Z"/>
    <path fill="var(--dark)" d="M0 1130C220 1090 520 1078 842 1128V1188H0Z"/>
  </svg>

  <div class="badge">
    <div class="badge-free">FREE</div>
    <div class="badge-line blue">ROOF INSPECTION</div>
    <div class="badge-line dark">NO OBLIGATION</div>
  </div>

  <div class="brand">
    <span class="brand-dot"></span>
    <span class="brand-name">Bellvane Plumbing<br>&amp; Gasfitting</span>
  </div>

  <h1 class="headline">
    <span class="grey line-1">Gutter &amp; Driveway</span>
    <span class="blue line-2">Cleaning</span>
    <span class="grey line-3">Roof &amp; Gutter</span>
    <span class="blue line-4">Repairs</span>
  </h1>

  <p class="other-services">All general plumbing maintenance' is offered as other services but not too much wording about this as the target is for gutter cleaning.</p>

  <div class="call">
    <div class="call-label">CALL US NOW</div>
    <div class="call-number">
      <svg class="call-icon" viewBox="0 0 20 20"><circle cx="10" cy="10" r="9" fill="var(--blue)"/><path fill="var(--white)" d="M7 5l2 2.5-1.2 1.3c.6 1.3 1.5 2.2 2.6 2.7L11.6 10l2.4 2-1 2c-3.5-.3-6.6-3.5-7-7z"/></svg>
      0427 386 915
    </div>
  </div>

  <section class="info-panel">
    <p class="info-lead">Prevent against flooding, mold, rust, rotting and corrosion now!</p>
    <h2 class="info-sub">Gutter Cleaning Services</h2>
    <ul class="checklist">
      <li><svg viewBox="0 0 14 14"><rect x="1" y="2" width="11" height="11" fill="none" stroke="var(--yellow)" stroke-width="1.5"/><path d="M3.5 7l2.5 2.5L13 1.5" fill="none" stroke="var(--yellow)" stroke-width="1.8"/></svg>Remove leaves, sticks, and other debris</li>
      <li><svg viewBox="0 0 14 14"><rect x="1" y="2" width="11" height="11" fill="none" stroke="var(--yellow)" stroke-width="1.5"/><path d="M3.5 7l2.5 2.5L13 1.5" fill="none" stroke="var(--yellow)" stroke-width="1.8"/></svg>Clear away clogs</li>
      <li><svg viewBox="0 0 14 14"><rect x="1" y="2" width="11" height="11" fill="none" stroke="var(--yellow)" stroke-width="1.5"/><path d="M3.5 7l2.5 2.5L13 1.5" fill="none" stroke="var(--yellow)" stroke-width="1.8"/></svg>Test your downpipes</li>
      <li><svg viewBox="0 0 14 14"><rect x="1" y="2" width="11" height="11" fill="none" stroke="var(--yellow)" stroke-width="1.5"/><path d="M3.5 7l2.5 2.5L13 1.5" fill="none" stroke="var(--yellow)" stroke-width="1.8"/></svg>Pinpoint any gutter issues</li>
      <li><svg viewBox="0 0 14 14"><rect x="1" y="2" width="11" height="11" fill="none" stroke="var(--yellow)" stroke-width="1.5"/><path d="M3.5 7l2.5 2.5L13 1.5" fill="none" stroke="var(--yellow)" stroke-width="1.8"/></svg>Repair gutter</li>
    </ul>
    <p class="info-close">With regular service, you can count on your property to be well-protected no matter what the forecast!</p>
  </section>

  <div class="price">
    <div class="price-inner">
      <div class="price-label">GUTTER CLEANING</div>
      <div class="price-amount">FROM <span>$199</span></div>
    </div>
  </div>

  <footer class="footer">
    <div class="footer-name">BELLVANE PLUMBING &amp; GASFITTING</div>
    <div class="footer-details">
      <span><b>License:</b> 3174520</span>
      <span><b>ABN:</b> 71904352816</span>
      <span><b>Web:</b> http://bellvaneplumbing.example-site.net/</span>
    </div>
  </footer>
</main>
</body>
</html>
```